Business cards for Norwegian software consultancy business

We are in need of business cards for our Norwegian consultancy company.
“Talvik Brensor AS” specializes in software development, architecture and agile methodology, providing mostly on-site services at customers.
The cards should reflect a certain level of business professionalism with an elegant touch, while paying tribute to our modern and technological heritage. Our logo should be featured, as well as room for basic information about the cardholder and legal information of the company (company name, address and VAT number).
We would like our cards to reflect that we are a modern consulting company. It should present a professional image that people will remember. The texture and color pallette should reflect our professionalism and reliability, so we prefer a light color pallette with colors such as gray, white, blue and black. The number of colors used should however not be overwhelming, with the text being distinct and readable.
We are open to untraditional layouts and playful designs as long as they communicate the intent stated above.
You could also take a look at our website http://www.brensor.no for input on our visual profile.
Our logo is attached in the form of vectors and rasterized PNG. Please comment if you would like the black-white and/or inverted versions as well.
Architecture
Company information:
Talvik Brensor AS
Lindeholtveien 7, 3142 Vestskogen
461 82 915
info@brensor.no
www.brensor.no
Employee information:
Full name
Title
Email
Phone

```html
<!DOCTYPE html>
<html lang="en">
<head>
<meta charset="utf-8">
<title>Talvik Brensor AS – Business Cards</title>
<link href="https://fonts.googleapis.com/css2?family=Arimo:wght@400;700&display=swap" rel="stylesheet">
<style>
  :root {
    --backdrop: #6f7a78;
    --card-black: #050505;
    --card-blue-top: #a7c8e6;
    --card-blue-bottom: #6aa3d6;
    --ink-white: #ffffff;
    --accent-blue: #6fa6dc;
    --tile-dark: #243040;
    --tile-light: rgba(255,255,255,0.28);
    --rule-white: rgba(255,255,255,0.85);
  }
  * { margin: 0; padding: 0; box-sizing: border-box; }
  html, body {
    width: 1200px; height: 900px; overflow: hidden;
    background: var(--backdrop);
    font-family: "Arimo", Arial, sans-serif;
  }
  .card {
    position: absolute;
    width: 600px; height: 343px;
    border-radius: 26px;
    overflow: hidden;
    box-shadow: 0 10px 30px rgba(0,0,0,0.35);
  }

  /* Back of card: light blue with contact details */
  .card--back {
    left: 540px; top: 70px;
    background: linear-gradient(180deg, var(--card-blue-top), var(--card-blue-bottom));
    color: var(--ink-white);
  }
  .card--back .divider-vertical {
    position: absolute; left: 300px; top: 0; width: 1px; height: 150px;
    background: var(--rule-white);
  }
  .card--back .divider-horizontal {
    position: absolute; left: 300px; right: 40px; top: 176px; height: 1px;
    background: var(--rule-white);
  }
  .card--back .divider-footer {
    position: absolute; left: 0; right: 0; top: 262px; height: 1px;
    background: var(--rule-white);
  }
  .cardholder {
    position: absolute; left: 330px; top: 92px;
    font-size: 15px; line-height: 1.25;
  }
  .cardholder__name { font-weight: 400; }
  .cardholder__title { font-weight: 700; }
  .contact-row {
    position: absolute; left: 150px; right: 40px; top: 205px;
    display: flex; gap: 14px; align-items: center;
    font-size: 15px; white-space: nowrap;
  }
  .contact-row svg { width: 14px; height: 14px; vertical-align: -2px; margin-right: 4px; }
  .address {
    position: absolute; right: 40px; top: 232px;
    font-size: 13px; font-weight: 700;
  }
  .wordmark {
    position: absolute;
    display: flex; align-items: center; gap: 12px;
    font-weight: 700; letter-spacing: 1px; white-space: nowrap;
  }
  .wordmark__square { display: inline-block; background: currentColor; }
  .card--back .wordmark { left: 40px; top: 150px; font-size: 26px; color: var(--ink-white); }
  .card--back .wordmark__square { width: 20px; height: 20px; }
  .tiles { position: absolute; }
  .card--back .tiles { right: 0; top: 80px; width: 200px; height: 100px; }

  /* Front of card: black with wordmark */
  .card--front {
    left: 60px; top: 490px;
    background: var(--card-black);
    color: var(--ink-white);
  }
  .card--front .wordmark { left: 90px; top: 148px; font-size: 36px; }
  .card--front .wordmark__square { width: 26px; height: 26px; color: var(--accent-blue); }
  .card--front .wordmark__text { color: var(--ink-white); }
  .card--front .tiles { right: 0; top: 60px; width: 180px; height: 140px; }
</style>
</head>
<body>

<section class="card card--back" aria-label="Business card, back">
  <div class="divider-vertical"></div>
  <div class="wordmark"><span class="wordmark__square"></span><span class="wordmark__text">Talvik Brensor</span></div>
  <div class="cardholder">
    <div class="cardholder__name">Lena Marsholt</div>
    <div class="cardholder__title">Co-Founder &amp; CEO</div>
  </div>
  <div class="tiles" role="img" aria-label="Soft square tile decoration"
       style="background: linear-gradient(90deg, rgba(255,255,255,0), var(--tile-light));"></div>
  <div class="divider-horizontal"></div>
  <div class="contact-row">
    <span><svg viewBox="0 0 14 14" aria-hidden="true"><rect x="3" y="1" width="8" height="12" rx="1.5" fill="none" stroke="#fff" stroke-width="1.4"/></svg>(047) 461-8291</span>
    <span><svg viewBox="0 0 14 14" aria-hidden="true"><rect x="1" y="3" width="12" height="8" fill="none" stroke="#fff" stroke-width="1.2"/><path d="M1 3l6 5 6-5" fill="none" stroke="#fff" stroke-width="1.2"/></svg>info@brensor.no</span>
    <span><svg viewBox="0 0 14 14" aria-hidden="true"><circle cx="7" cy="7" r="5.5" fill="none" stroke="#fff" stroke-width="1.2"/><path d="M1.5 7h11M7 1.5c-3 3-3 8 0 11M7 1.5c3 3 3 8 0 11" fill="none" stroke="#fff" stroke-width="1"/></svg>brensor.no</span>
  </div>
  <div class="address">Lindeholtveien 7 / 3142 Vestskogen</div>
  <div class="divider-footer"></div>
</section>

<section class="card card--front" aria-label="Business card, front">
  <div class="wordmark"><span class="wordmark__square"></span><span class="wordmark__text">Talvik Brensor</span></div>
  <div class="tiles" role="img" aria-label="Soft square tile decoration"
       style="background: linear-gradient(90deg, rgba(36,48,64,0), var(--tile-dark));"></div>
</section>

</body>
</html>
```